Web Site - Harbor-Lift.com

Design a 3 page web site for Harbor Lift. See attached design brief.
Harbor Lift - Web Site
www.harbor-lift.com

Design a 3 page web site for Harbor Lift, a small local fitness center that provided cardio and weights only (machines and free weights). There are no classes or other services offered at this facility. Harbor Lift is an affordable alternative to the big box, expensive fitness centers. It is small, local, convenient and a community oriented place to work out.
web site can be clean, simple and communicate basic information about the company and membership offers. Although the branding is black, orange and gray, the web site colors should be soft, light and neutral colors that will appeal to both men and women.
Text: Input generic text during design for each text area that will be modified later during the coding phase. The selected designer is expected to code the site and deliver all compressive files (images, files and code) for an unrestricted hand off and full ownership of all content by the client for future modifications by others.

Images
Images used can be generic royalty free images of people working out, on cardio machines, lifting on universal equipment, stretching or lifting weights or images with out people i.e a yoga mat, free weights, a row of cardio machines etc. This is an adults only facility - images can be a mix of men and women and of diverse multi ethnic backgrounds. Image of the actual gym are included below but should NOT be used on the web site.

Branding - See attached for vertical and horizontal logos for Harbor Lift. These can be used in any way and should be incorporated into the web site
WEB SITE OUTLINE
THREE web pages - Pages can be individual pages clicked through to each page from a navigation area but ALSO pages can be “blend together” into one long scrolling “home” or primary landing page.
1) Home Page with basic information
2) Membership Page (to be later integrated with Quellon member software to show changing membership specials). - see example below - all text will change later
3) contact page - address - telephone number - google map directions
www.harbor-lift.com
Address:
Located in Tolvern Brook Plaza
518 E. Marlow Lane, Suite 104, Brenholt PA 19052
Tel: 484-555-0172

Target Market(s)

Men and Women - Adults over 18,

Industry/Entity Type

Fitness, Work Out, Gym

Coding

Coded - Design and coding required

Number of Pages Required

3 page

Requirements
Must have
• See Project Brief
Should not have
• Dark Colors that feel too masculine

```html
<!DOCTYPE html>
<html lang="en">
<head>
<meta charset="utf-8">
<title>Harbor Lift – Contact</title>
<link href="https://fonts.googleapis.com/css2?family=Oswald:wght@300;400;500;600;700&family=Inter:wght@400;500;600&display=swap" rel="stylesheet">
<style>
:root{
  --orange:#f26a10;
  --dark:#2d2d2d;
  --ink:#1b1b1b;
  --text:#444;
  --muted:#6b6b6b;
  --line:#cfcfcf;
  --soft:#f6f5f3;
  --white:#fff;
}
*{box-sizing:border-box;margin:0;padding:0}
html,body{width:1200px;height:3824px;overflow:hidden}
body{position:relative;background:var(--white);font-family:"Inter",sans-serif;color:var(--text)}
.abs{position:absolute}
.display{font-family:"Oswald",sans-serif;font-weight:700;text-transform:uppercase;color:var(--ink);line-height:1.08}
.accent{color:var(--orange)}

/* top bar */
.topbar{left:0;top:0;width:1200px;height:52px;background:var(--white)}
.topbar .contact{right:213px;top:9px;text-align:right;font-family:"Oswald",sans-serif;font-size:13px;line-height:17px;color:var(--ink)}
.dots{right:58px;top:17px;display:flex;gap:16px}
.dots span{width:18px;height:18px;border:1.6px solid var(--ink);border-radius:50%}

/* nav */
.nav{left:0;top:52px;width:1200px;height:86px;background:var(--dark)}
.brand{display:flex;align-items:center;gap:10px;font-family:"Oswald",sans-serif;font-weight:600;font-size:27px;letter-spacing:2px;color:var(--white)}
.brand i{width:22px;height:22px;background:var(--orange);display:block}
.nav .brand{left:49px;top:24px}
.menu{left:265px;top:33px;display:flex;gap:28px;font-family:"Oswald",sans-serif;font-size:14px;color:#ddd}
.menu .on{color:var(--orange);border-bottom:2px solid var(--orange);padding-bottom:3px}
.nav .call{left:882px;top:33px;font-family:"Oswald",sans-serif;font-size:14px;color:var(--white);border-bottom:2px solid #ddd;padding-bottom:6px}
.btn{display:inline-flex;align-items:center;justify-content:center;background:var(--orange);color:var(--white);font-family:"Oswald",sans-serif;font-size:14px;border-radius:5px}
.nav .btn{left:972px;top:23px;width:187px;height:45px}

/* hero */
.hero{left:0;top:138px;width:1200px;height:552px;background:linear-gradient(90deg,#1d2430 0%,#2a3240 38%,#8a6a55 62%,#c98a6a 78%,#b0a040 100%)}
.hero .shade{inset:0;background:linear-gradient(90deg,rgba(20,26,36,.92) 0%,rgba(20,26,36,.7) 40%,rgba(20,26,36,0) 70%)}
.hero h1{left:41px;top:108px;font-size:88px;color:var(--white);line-height:1}
.hero p{left:41px;top:308px;width:640px;font-size:19.5px;line-height:33px;color:#eee}
.hero .btn{left:41px;top:412px;width:187px;height:45px}
.ghost{left:248px;top:412px;width:175px;height:45px;border:1.5px solid var(--white);border-radius:5px;color:var(--white);font-family:"Oswald",sans-serif;font-size:14px;display:flex;align-items:center;justify-content:center}

/* contact form */
.mapcard{left:53px;top:826px;width:517px;height:644px;background:#fdfcfb;box-shadow:0 0 24px rgba(0,0,0,.05)}
.map{left:71px;top:845px;width:481px;height:536px;background:linear-gradient(135deg,#e7ede4,#f1efe8 50%,#e5ebe6)}
.mapcard .addr{left:0;top:574px;width:517px;text-align:center;font-size:22px;line-height:38px;color:#555}
.ask{left:616px;top:812px;font-size:57px}
.intro{left:616px;top:958px;width:560px;font-family:"Oswald",sans-serif;font-weight:300;font-size:19px;line-height:30px;color:#555}
.lbl{font-family:"Oswald",sans-serif;font-size:13px;color:var(--ink)}
.field{border:1px solid var(--line);border-radius:5px;background:#f7f7f7;font-family:"Oswald",sans-serif;font-weight:300;font-size:13px;color:#666;padding:0 10px;display:flex;align-items:center}
.textarea{align-items:flex-start;padding-top:14px}
.check{left:616px;top:1413px;display:flex;align-items:center;gap:8px;font-family:"Oswald",sans-serif;font-size:12px;color:var(--ink)}
.check i{width:15px;height:15px;border:1px solid #777;border-radius:3px;display:block}
.send{left:616px;top:1462px;width:539px;height:45px}

/* contact details */
.details{left:0;top:1622px;width:1200px;height:646px;background:var(--soft)}
.details h2{left:54px;top:84px;font-size:58px}
.details p{left:54px;top:168px;width:800px;font-family:"Oswald",sans-serif;font-weight:300;font-size:19px;line-height:30px;color:#444}
.card{top:325px;width:338px;height:237px;background:var(--white);border-radius:3px}
.card .ico{left:20px;top:20px;width:46px;height:46px;background:#fdece1;display:flex;align-items:center;justify-content:center}
.card h3{left:20px;top:94px;font-family:"Oswald",sans-serif;font-weight:600;font-size:28px;color:var(--ink)}
.card .info{left:20px;top:142px;font-family:"Oswald",sans-serif;font-weight:300;font-size:13px;line-height:20px;color:#333}
.card .link{left:20px;text-decoration:underline;font-family:"Oswald",sans-serif;font-size:13px;color:var(--ink)}

/* faq */
.eyebrow{left:0;top:2386px;width:1200px;text-align:center;font-family:"Oswald",sans-serif;font-size:20px;color:var(--ink)}
.faq-title{left:0;top:2428px;width:1200px;text-align:center;font-size:60px}
.faq-sub{left:0;top:2512px;width:1200px;text-align:center;font-family:"Oswald",sans-serif;font-weight:300;font-size:20px;color:var(--ink)}
.faq-photo{left:105px;top:2577px;width:418px;height:598px;border-radius:32px;background:linear-gradient(160deg,#cfcac2,#a59c90 55%,#6d6660)}
.pill{left:130px;top:3087px;width:372px;height:62px;border-radius:31px;background:var(--orange);color:var(--white);font-family:"Oswald",sans-serif;font-weight:600;font-size:21px;display:flex;align-items:center;justify-content:center}
.faq{left:576px;top:2596px;width:504px}
.q{position:relative;height:59.3px;font-family:"Oswald",sans-serif;font-weight:300;font-size:20px;color:var(--ink);padding-top:14px}
.q svg{position:absolute;right:2px;top:22px}
.q.open{height:120px;font-family:"Inter",sans-serif;font-weight:400;font-size:19px;padding-top:0}
.q.open p{font-size:15.5px;line-height:26px;color:#555;margin-top:6px;width:420px}
.q.open svg{top:26px}

/* footer */
.footer{left:0;top:3290px;width:1200px;height:534px;background:#333;color:#ccc}
.footer .brand{left:104px;top:113px}
.tag{left:93px;top:208px;width:220px;font-size:12.5px;line-height:20px;color:#bbb}
.fcol{top:113px;font-size:12px;line-height:17px;color:#ddd}
.fcol h4{font-size:13px;font-weight:600;color:var(--white);margin-bottom:20px;letter-spacing:.3px}
.fcol li{list-style:none;margin-bottom:14px}
.sub p{width:320px;font-size:13px;line-height:20px;color:#ddd}
.sub-input{left:716px;top:200px;width:222px;height:41px;border:1px solid #888;font-size:13px;color:#888;display:flex;align-items:center;padding-left:10px}
.sub-btn{left:949px;top:200px;width:101px;height:41px;border:1px solid #bbb;font-size:13px;color:var(--white);display:flex;align-items:center;justify-content:center}
.fine{left:716px;top:252px;width:340px;font-size:9.5px;line-height:15px;color:#ccc}
.fine u{color:#ddd}
.bottom{left:53px;top:452px;display:flex;gap:20px;font-size:12px;color:#ddd}
.bottom u{color:#ddd}
.fdots{right:58px;top:450px;display:flex;gap:13px}
.fdots span{width:16px;height:16px;border-radius:50%;background:#eee;display:block}
</style>
</head>
<body>

<header class="abs topbar">
  <div class="abs contact">484-555-0172<br>info@harborlift.com</div>
  <div class="abs dots" aria-label="Social links"><span></span><span></span><span></span></div>
</header>

<nav class="abs nav">
  <div class="abs brand"><i></i>HARBOR LIFT</div>
  <div class="abs menu"><span>HOME</span><span>MEMBERSHIP</span><span>BLOGS</span><span class="on">CONTACT</span></div>
  <div class="abs call">CALL NOW</div>
  <div class="abs btn">VIEW MEMBERSHIP OPTIONS</div>
</nav>

<section class="abs hero">
  <div class="abs" role="img" aria-label="Group of smiling adults stacking hands together in the gym" style="inset:0"></div>
  <div class="abs shade"></div>
  <h1 class="abs display">Visit <span class="accent">Harbor Lift</span><br>in Brenholt, PA</h1>
  <p class="abs">Conveniently located in Tolvern Brook Plaza, we’re your local, affordable destination for cardio and strength training.</p>
  <div class="abs btn">VIEW MEMBERSHIP OPTIONS</div>
  <div class="abs ghost">CALL NOW&nbsp; 484-555-0172</div>
</section>

<section>
  <div class="abs mapcard"><div class="abs addr">518 E. Marlow Lane, Suite 104,<br>Brenholt, PA 19052</div></div>
  <div class="abs map" role="img" aria-label="Street map showing the gym location in the plaza"></div>

  <h2 class="abs display ask">Have a <span class="accent">question?</span><br>We’re here <span class="accent">to help.</span></h2>
  <p class="abs intro">Whether you’re interested in membership options or just want to learn more about our facility, send us a message and we’ll get back to you shortly.</p>

  <div class="abs lbl" style="left:616px;top:1044px">Full Name</div>
  <div class="abs field" style="left:616px;top:1069px;width:260px;height:40px">John Doe</div>
  <div class="abs lbl" style="left:894px;top:1044px">Email Address</div>
  <div class="abs field" style="left:894px;top:1069px;width:261px;height:40px">john@example.com</div>

  <div class="abs lbl" style="left:616px;top:1131px">Subject</div>
  <div class="abs field" style="left:616px;top:1155px;width:539px;height:40px;justify-content:space-between">Membership Inquiry
    <svg width="14" height="9" viewBox="0 0 14 9"><path d="M1 1l6 6 6-6" fill="none" stroke="#222" stroke-width="1.8"/></svg></div>

  <div class="abs lbl" style="left:616px;top:1217px">Your Message</div>
  <div class="abs field textarea" style="left:616px;top:1241px;width:539px;height:151px">How can we help you?</div>

  <div class="abs check"><i></i>I accept the <u>Terms</u></div>
  <div class="abs btn send">Send Message</div>
</section>

<section class="abs details">
  <h2 class="abs display"><span class="accent">Contact</span> Details</h2>
  <p class="abs">Harbor Lift is conveniently located in Tolvern Brook Plaza, making it easy for local residents to access a clean, community-focused gym without the crowds of large corporate fitness centers. We’re proud to serve the Brenholt area with affordable cardio and strength training options in a welcoming, adults-only environment.</p>

  <div class="abs card" style="left:53px">
    <div class="abs ico"><svg width="30" height="30" viewBox="0 0 24 24"><path d="M12 22s7-6.5 7-12a7 7 0 0 0-14 0c0 5.5 7 12 7 12z" fill="none" stroke="#f26a10" stroke-width="1.8"/><circle cx="12" cy="10" r="2.6" fill="none" stroke="#f26a10" stroke-width="1.8"/></svg></div>
    <h3 class="abs">Visit Us</h3>
    <div class="abs info">Tolvern Brook Plaza<br>518 E. Marlow Lane, Suite 104, Brenholt PA 19052</div>
    <div class="abs link" style="top:196px">Pennsylvania, UNITED STATES</div>
  </div>
  <div class="abs card" style="left:431px">
    <div class="abs ico"><svg width="30" height="30" viewBox="0 0 24 24"><path d="M5 3h4l2 5-2.5 1.5a11 11 0 0 0 6 6L16 13l5 2v4a2 2 0 0 1-2 2A16 16 0 0 1 3 5a2 2 0 0 1 2-2z" fill="none" stroke="#f26a10" stroke-width="1.8" stroke-linejoin="round"/></svg></div>
    <h3 class="abs">Call Us</h3>
    <div class="abs info">484-555-0172</div>
    <div class="abs link" style="top:182px">Support: Mon-Friday, 9am-5pm</div>
  </div>
  <div class="abs card" style="left:808px">
    <div class="abs ico" style="top:30px"><svg width="32" height="26" viewBox="0 0 26 20"><rect x="1" y="1" width="24" height="18" rx="2" fill="none" stroke="#f26a10" stroke-width="1.8"/><path d="M1 3l12 8 12-8" fill="none" stroke="#f26a10" stroke-width="1.8"/></svg></div>
    <h3 class="abs" style="top:106px">Email Us</h3>
    <div class="abs info" style="left:23px;top:154px">info@harborlift.com</div>
    <div class="abs link" style="top:194px">Response within 2 hours</div>
  </div>
</section>

<section>
  <div class="abs eyebrow">COMMON QUESTION</div>
  <h2 class="abs display faq-title">Frequently asked <span class="accent">questions</span></h2>
  <div class="abs faq-sub">Take the first step toward a healthier, stronger you.</div>
  <div class="abs faq-photo" role="img" aria-label="Trainer reviewing a workout plan with a member on a clipboard"></div>
  <div class="abs pill">HELPING YOU EVERY STEP OF THE WAY.</div>

  <div class="abs faq">
    <div class="q open">Are there any group classes?<p>No, Harbor Lift focuses only on cardio and weight training equipment.</p>
      <svg width="14" height="9" viewBox="0 0 14 9"><path d="M1 1l6 6 6-6" fill="none" stroke="#222" stroke-width="2"/></svg></div>
    <div class="q">Do you provide personal training?<svg width="14" height="9" viewBox="0 0 14 9"><path d="M1 8l6-6 6 6" fill="none" stroke="#222" stroke-width="2"/></svg></div>
    <div class="q">Are memberships month-to-month?<svg width="14" height="9" viewBox="0 0 14 9"><path d="M1 8l6-6 6 6" fill="none" stroke="#222" stroke-width="2"/></svg></div>
    <div class="q">Is the gym adults-only?<svg width="14" height="9" viewBox="0 0 14 9"><path d="M1 8l6-6 6 6" fill="none" stroke="#222" stroke-width="2"/></svg></div>
    <div class="q">What are your operating hours?<svg width="14" height="9" viewBox="0 0 14 9"><path d="M1 8l6-6 6 6" fill="none" stroke="#222" stroke-width="2"/></svg></div>
    <div class="q">Do I need to bring my own equipment?<svg width="14" height="9" viewBox="0 0 14 9"><path d="M1 8l6-6 6 6" fill="none" stroke="#222" stroke-width="2"/></svg></div>
    <div class="q">Can I try the gym before signing up?<svg width="14" height="9" viewBox="0 0 14 9"><path d="M1 8l6-6 6 6" fill="none" stroke="#222" stroke-width="2"/></svg></div>
    <div class="q">Is parking available?<svg width="14" height="9" viewBox="0 0 14 9"><path d="M1 8l6-6 6 6" fill="none" stroke="#222" stroke-width="2"/></svg></div>
    <div class="q">What payment methods do you accept?<svg width="14" height="9" viewBox="0 0 14 9"><path d="M1 8l6-6 6 6" fill="none" stroke="#222" stroke-width="2"/></svg></div>
  </div>
</section>

<footer class="abs footer">
  <div class="abs brand"><i></i>HARBOR LIFT</div>
  <p class="abs tag">Clear Pricing With No Hidden Fees Or Surprises.</p>

  <div class="abs fcol" style="left:325px;width:180px">
    <h4>RECENT BLOG</h4>
    <ul><li>Build Strength with Simple Free Weight Routines</li><li>Maximize Your Cardio Workout for Better Endurance</li><li>Creating a Balanced Weekly Workout Plan</li><li>Creating a Balanced Weekly Workout Plan</li><li>Creating a Balanced Weekly Workout Plan</li></ul>
  </div>
  <div class="abs fcol" style="left:530px">
    <h4>QUICK LINKS</h4>
    <ul><li>Home</li><li>Membership</li><li>Blogs</li><li>contact</li></ul>
  </div>
  <div class="abs fcol sub" style="left:716px">
    <h4>SUBSCRIBE</h4>
    <p>Join our newsletter to stay up to date on features and releases.</p>
  </div>
  <div class="abs sub-input">Enter your email</div>
  <div class="abs sub-btn">Subscribe</div>
  <p class="abs fine">By subscribing you agree to with our <u>Privacy Policy</u> and provide consent to receive updates from our company.</p>

  <div class="abs bottom"><span>© 2026 Harbor Lift. All rights reserved.</span><u>Privacy Policy</u><u>Terms of Service</u><u>Cookies Settings</u></div>
  <div class="abs fdots" aria-label="Social links"><span></span><span></span><span></span><span></span><span></span></div>
</footer>

</body>
</html>
```